Dallas Texas Special Event Center Flyer

Need a new brochure (small 8.5 x 11 tri-fold) for an event center in Dallas, Texas area. It is located on a golf course and is ideal for weddings, quinceaneras, retirement parties, etc. Is best known for weddings. There is no logo for the event center. I have attached the prior brochure, which is not professional. We do not have any site photos.

Target Market(s)

people seeking special event space in dallas, texas area. Brides, meeting planners, etc.

Industry/Entity Type

Golf Course

Font styles to use
Script
Other font styles liked:
• combine serif and some use of script ok

Requirements
Must have
• lots of photos - see attached

```html
<!DOCTYPE html>
<html lang="en">
<head>
<meta charset="utf-8">
<title>Special Event Center in Dallas – Brochure</title>
<link href="https://fonts.googleapis.com/css2?family=Lato:wght@400;700&family=Lobster&family=Courgette&display=swap" rel="stylesheet">
<style>
  :root{
    --magenta:#a3138e;
    --ink:#1e1e1e;
    --black:#0a0a0a;
    --paper:#efefef;
    --stage:#d9d9d9;
  }
  html,body{margin:0;padding:0;width:1200px;height:900px;overflow:hidden;background:var(--stage);}
  .brochure{position:absolute;left:40px;top:14px;width:1120px;height:872px;overflow:hidden;background:var(--paper);}
  .brochure-shapes{position:absolute;left:0;top:0;width:1120px;height:872px;}
  .intro{position:absolute;left:43px;top:318px;width:311px;font:400 16px/21px "Lato",sans-serif;color:var(--ink);text-align:justify;hyphens:auto;}
  .intro p{margin:0 0 20px;}
  .contact{position:absolute;left:386px;top:358px;width:300px;font-family:"Lato",sans-serif;color:var(--ink);}
  .contact-heading{margin:0 0 14px;font-weight:700;font-size:18px;line-height:22px;color:var(--magenta);}
  .contact-line{display:flex;align-items:center;gap:6px;margin:0;}
  .contact-web{font-size:15px;line-height:22px;padding-left:16px;}
  .contact-mail{font-size:11px;line-height:16px;}
  .contact-phone{font-size:18px;line-height:23px;}
  .contact-address{font-size:15px;line-height:21px;margin-top:18px;padding-left:16px;}
  .icon{width:10px;height:10px;flex:none;}
  .headline{position:absolute;left:742px;top:510px;width:360px;text-align:center;}
  .headline-script{margin:0;font-family:"Lobster",cursive;font-size:86px;line-height:86px;color:var(--magenta);}
  .headline-sub{margin:0;font-family:"Courgette",cursive;font-size:44px;line-height:52px;color:var(--ink);}
</style>
</head>
<body>
<main class="brochure">
  <svg class="brochure-shapes" viewBox="0 0 835 650" xmlns="http://www.w3.org/2000/svg">
    <defs>
      <linearGradient id="paper-glow" x1="0" y1="0" x2="1" y2="0">
        <stop offset="0" stop-color="#e6e4e2"/>
        <stop offset="0.5" stop-color="#d8d6d4"/>
        <stop offset="1" stop-color="#f4f4f4"/>
      </linearGradient>
      <linearGradient id="toast-tone" x1="0" y1="0" x2="1" y2="1">
        <stop offset="0" stop-color="#c9a48a"/>
        <stop offset="0.5" stop-color="#d8c6ae"/>
        <stop offset="1" stop-color="#8f7a66"/>
      </linearGradient>
      <linearGradient id="couple-tone" x1="0" y1="0" x2="1" y2="1">
        <stop offset="0" stop-color="#e8ede2"/>
        <stop offset="0.5" stop-color="#9fb07a"/>
        <stop offset="1" stop-color="#5e6b3f"/>
      </linearGradient>
      <radialGradient id="cake-tone" cx="0.5" cy="0.45" r="0.6">
        <stop offset="0" stop-color="#f4efea"/>
        <stop offset="0.6" stop-color="#d9c8c8"/>
        <stop offset="1" stop-color="#2b2424"/>
      </radialGradient>
    </defs>

    <rect class="paper" width="835" height="650" fill="url(#paper-glow)"/>

    <path class="photo-toast" role="img" aria-label="Photo: bride and guests raising champagne glasses in a toast"
      d="M0 0 H425 C410 60 400 130 410 225 C300 200 200 205 120 170 C60 145 20 115 0 95 Z" fill="url(#toast-tone)"/>
    <path class="accent-curve" d="M0 95 C20 115 60 145 120 170 C200 205 300 200 410 225" fill="none" stroke="var(--magenta)" stroke-width="6"/>

    <path class="photo-couple" role="img" aria-label="Photo: newlywed couple walking down the aisle under falling petals"
      d="M495 0 H835 V320 C760 345 640 350 580 300 C520 250 495 130 495 0 Z" fill="url(#couple-tone)"/>
    <path class="accent-curve" d="M495 0 C495 130 520 250 580 300 C640 350 760 345 835 320" fill="none" stroke="var(--magenta)" stroke-width="7"/>

    <path class="base-band" d="M0 560 C140 580 250 570 310 548 L545 522 C640 560 740 570 835 552 V650 H0 Z" fill="var(--black)"/>
    <path class="accent-band" d="M0 552 C140 572 250 562 310 540" fill="none" stroke="var(--magenta)" stroke-width="12"/>
    <path class="accent-band" d="M545 514 C640 552 740 562 835 544" fill="none" stroke="var(--magenta)" stroke-width="12"/>

    <circle class="photo-cake" role="img" aria-label="Photo: white wedding cake decorated with pink and white roses"
      cx="420" cy="557" r="124" fill="url(#cake-tone)" stroke="var(--magenta)" stroke-width="8"/>
  </svg>

  <section class="intro">
    <p>The Event Hall at Willowbend offers a 12,000 square foot facility which boasts a Grand Ballroom and two Banquet Rooms. The grand ballroom will accommodate 809 guests for a wedding ceremony and reception</p>
    <p>The Event Hall at Willowbend is the perfect location for your wedding, conference, seminar, party, reunion, or graduation.</p>
    <p>The Event Hall at Willowbend is located on Willowbend Golf Course, an 18-hole, 215-acre Championship golf course in Crandall, Texas, and is surrounded by rolling hills, seven lakes, creeks, pecan orchards, and many varieties of wildlife.</p>
  </section>

  <section class="contact">
    <h2 class="contact-heading">Contact us for more information<br>or visit us a:</h2>
    <p class="contact-line contact-web">www.eventhallatwillowbend.com</p>
    <p class="contact-line contact-mail">
      <svg class="icon" viewBox="0 0 10 10"><circle cx="5" cy="5" r="4.2" fill="none" stroke="var(--magenta)" stroke-width="1.2"/><path d="M1 5H9M5 1C3 3 3 7 5 9M5 1C7 3 7 7 5 9" fill="none" stroke="var(--magenta)" stroke-width="0.8"/></svg>
      dana marsh dana@eventhallatwillowbend.com
    </p>
    <p class="contact-line contact-phone">
      <svg class="icon" viewBox="0 0 10 10"><rect width="10" height="10" rx="2" fill="var(--magenta)"/><path d="M3 2.3L4.2 3.6 3.6 4.4C4 5.3 4.7 6 5.6 6.4L6.4 5.8 7.7 7 7 7.8C4.6 7.6 2.4 5.4 2.2 3Z" fill="#fff"/></svg>
      214-555-0186
    </p>
    <p class="contact-line contact-phone">
      <svg class="icon" viewBox="0 0 10 10"><rect width="10" height="10" rx="2" fill="var(--magenta)"/><path d="M3 2.3L4.2 3.6 3.6 4.4C4 5.3 4.7 6 5.6 6.4L6.4 5.8 7.7 7 7 7.8C4.6 7.6 2.4 5.4 2.2 3Z" fill="#fff"/></svg>
      972-555-0142
    </p>
    <p class="contact-line contact-address">Event Hall at Willowbend 4810 E<br>Ridge Road Crandall, TX 75199</p>
  </section>

  <header class="headline">
    <h1 class="headline-script">Special</h1>
    <p class="headline-sub">Event Center</p>
    <p class="headline-sub">in Dallas</p>
  </header>
</main>
</body>
</html>
```